Commercial Roof Management Brochure

TKV Group www.tkvgroup-demo.io is a Commercial and Industrial roof consulting company. We are looking to launch a new program to our customers. It is a roof maintenance service contract. Instead of paying for each service when needed we are bundling all the services under an annual maintenance contract. This will provide our clients with better value and service for their money. The brochure is something we would use to; email, mail or print and leave behind. It should be 1-2 pages. please incorporate our logo without the "roof and pavement consulting" text. Also include the Industry logos at the bottom somewhere PLWN and BXT. Stick with our colour scheme from our logo and website.

Target Market(s)

Industrial and commercial property management companies, real estate holding companies, REIT companies

Industry/Entity Type

Property Maintenance

Requirements
Must have
• our logo, professional design, creates interest
Nice to have
• follow our colors from the company logo

```html
<!DOCTYPE html>
<html lang="en">
<head>
<meta charset="utf-8">
<title>TKV Group – Roof Management Program</title>
<link href="https://fonts.googleapis.com/css2?family=Lato:wght@400;700;900&display=swap" rel="stylesheet">
<style>
  :root {
    --brand-red: #e8202a;
    --brand-blue: #0e5196;
    --footer-yellow: #ffe21f;
    --ink: #1d1d1f;
    --paper: #f7f7f8;
    --asphalt-dark: #3a3336;
    --asphalt-mid: #5b5356;
    --sky: #b9b3ad;
  }
  * { box-sizing: border-box; margin: 0; padding: 0; }
  html, body { width: 848px; height: 1200px; overflow: hidden; background: #fff; }
  body { font-family: "Lato", Arial, sans-serif; color: var(--ink); }

  .brochure {
    position: relative;
    width: 848px; height: 1200px;
    background: var(--brand-red);
    overflow: hidden;
  }
  .content-panel {
    position: absolute;
    left: 14px; top: 14px; width: 820px; height: 1052px;
    background: var(--paper);
  }
  .hero-photo {
    position: absolute;
    left: 14px; top: 14px; width: 820px; height: 521px;
    background: linear-gradient(180deg, var(--sky) 0%, #8a8180 6%, var(--asphalt-mid) 14%, var(--asphalt-dark) 55%, #4a4245 100%);
  }
  .hero-banner {
    position: absolute; left: 0; top: 260px;
    width: 848px; height: 290px;
  }
  .headline {
    position: absolute;
    left: 30px; top: 325px; width: 700px;
    color: #fff;
    font-weight: 700;
    font-size: 47px;
    line-height: 50px;
    text-align: center;
    transform: rotate(-3.6deg);
    transform-origin: center;
  }

  .intro {
    position: absolute;
    left: 72px; top: 563px; width: 705px;
    font-size: 14.4px; line-height: 20.6px;
    text-align: justify;
    text-align-last: center;
  }

  .value-column {
    position: absolute;
    left: 35px; top: 730px; width: 354px;
  }
  .value-title {
    color: var(--brand-red);
    font-weight: 900;
    font-size: 25px;
    letter-spacing: -0.3px;
    line-height: 28px;
    margin-bottom: 6px;
  }
  .value-text {
    font-size: 14.4px; line-height: 20.6px;
    text-align: justify;
  }

  .member-badges {
    position: absolute; left: 100px; top: 970px;
    width: 240px; height: 78px;
  }

  .manager-column {
    position: absolute;
    left: 409px; top: 730px; width: 415px;
  }
  .manager-title {
    color: var(--brand-blue);
    font-weight: 700;
    font-size: 25.5px; line-height: 29px;
    text-align: justify;
    text-align-last: left;
    margin-bottom: 12px;
  }
  .duty-list { list-style: none; padding-left: 14px; }
  .duty-list li {
    position: relative;
    padding-left: 14px;
    font-size: 14.4px; line-height: 17.5px;
    margin-bottom: 6.5px;
  }
  .duty-list li::before {
    content: "";
    position: absolute; left: 0; top: 5px;
    width: 7px; height: 7px; border-radius: 50%;
    background: var(--brand-red);
  }

  .contact-footer {
    position: absolute;
    left: 0; top: 1078px; width: 848px;
    color: var(--footer-yellow);
    font-size: 23.5px; line-height: 34.5px;
    text-align: center;
  }
</style>
</head>
<body>
<main class="brochure">
  <div class="content-panel"></div>

  <div class="hero-photo" role="img" aria-label="Photo of a worker sweeping gravel on a flat commercial roof, with repair spots circled in red paint"></div>

  <svg class="hero-banner" viewBox="0 0 848 290" aria-hidden="true">
    <polygon points="0,63 803,6 738,275 0,275" fill="var(--brand-red)"/>
    <polygon points="0,74 789,21 729,252 0,257" fill="var(--brand-blue)"/>
  </svg>

  <h1 class="headline">1 contact for all<br>your roofs = less confusion<br>and faster response times</h1>

  <p class="intro">A good roof maintenance program will keep tenants happy and preserve the value of your investment. By hiring us as your roof management firm you gain access to both in-house roof consulting staff, as well as their network of licensed, bonded and insured contractors who have already been vetted for good pricing and quality work. This can translate into significant savings compared to going through the yellow pages and hiring a roofer yourself. Not only is our firm able to get volume discounts on the work, we also know the contractors and understand maintenance issues such that they are capable of intelligently supervising the work.</p>

  <section class="value-column">
    <h2 class="value-title">INCREASED VALUE</h2>
    <p class="value-text">Preventative maintenance is achieved through putting systems in place that catch and deal with maintenance and repair issues early on, before they grow into larger more costly problems. This requires a written maintenance check program, detailed maintenance documentation and regular maintenance visits. You will have a dedicated roof manager assigned to your buildings.</p>
  </section>

  <svg class="member-badges" viewBox="0 0 240 78" role="img" aria-label="BXT and PLWN association membership badges">
    <rect x="9" y="10" width="64" height="60" rx="3" fill="#3f74b8"/>
    <ellipse cx="186" cy="40" rx="48" ry="33" fill="none" stroke="var(--brand-blue)" stroke-width="3"/>
  </svg>

  <section class="manager-column">
    <h2 class="manager-title">Your assigned roof manager is responsible for:</h2>
    <ul class="duty-list">
      <li>Perform and document semi-annual roof inspections including infrared moisture surveys.</li>
      <li>Respond to roof leaks, investigate and manage roofers to ensure safety, costs and quality</li>
      <li>Create documented maintenance plans for each building and execute</li>
      <li>Identify, document, tender and manage all repairs</li>
      <li>Prepare budgets for each building in your portfolio</li>
      <li>Write specifications for replacements</li>
      <li>Tender and manage all replacements with the utmost care for safety and your tenants</li>
    </ul>
  </section>

  <footer class="contact-footer">
    For more information or to sign up please contact TKV Group at<br>
    555-201-4830 || info@tkvgroup-demo.io<br>
    www.tkvgroup-demo.io
  </footer>
</main>
</body>
</html>
```